Flyer für Bürgerenergiegemeinschaft
Zielgruppe
Als Bürgerenergiegemeinschaft sind wir für unsere Bürgerinnen und Bürger die erste Anlaufstelle wenn es um sauberen regionalen erneuerbaren Strom geht. Mehr Infos unter www.kwl-rax.example
Aufgabenstellung
Ziel soll ein Falzflyer DL (220x110mm) mit Wickelfalz von Drucklo (https://www.drucklomat.example/marketingmaterial/falzflyer) sein. Bitte daher die Designrichtlinien von Drucklo beachten. Ausgefaltet hat der Flyer dann 297x210mm, gefaltet 99x210mm. Somit sind 6 kleine Seiten zu befüllen.
Auf diesen 6 Seiten soll der Inhalt unserer Webseite www.kwl-rax.example im gleichen Look übersichtlich aufbereitet werden.
Auf der gefalteten Rückseite sollen im unterne Bereich die nicht ausgefüllten Felder des Online-Rechners sein,
damit man im Kundengespräch die Werte die der Rechner ausgibt auf den Flyer niederschreiben kann den der Kunde dann mitbekommt.
Bilder können von der Webseite geladen werden oder von uns zur Verfügung gestellt werden.

```html
<!DOCTYPE html>
<html lang="de">
<head>
<meta charset="utf-8">
<title>KWLRAX Falzflyer</title>
<link href="https://fonts.googleapis.com/css2?family=Nunito:wght@400;600;700;800;900&display=swap" rel="stylesheet">
<style>
:root{
  --brand:#0ea5dc;
  --ink:#14172b;
  --grey:#666a70;
  --field:#eef6fc;
  --white:#ffffff;
  --photo-dark:#2d4460;
  --photo-light:#7f93ab;
  --trim:#d2383c;
  --bleed:#2c4486;
  --safe:#1e9a3a;
  --fold:#c6356a;
}
*{margin:0;padding:0;box-sizing:border-box}
html,body{width:1200px;height:855px;overflow:hidden;background:#fff}
body{font-family:'Nunito',sans-serif;color:var(--ink)}
.sheet{position:relative;width:1200px;height:855px;overflow:hidden;background:var(--white)}
.panel{position:absolute;top:0;height:855px;width:396px}
.panel--about{left:0}
.panel--calc{left:396px}
.panel--cover{left:792px;width:408px}
.eyebrow{position:absolute;left:0;right:0;top:58px;text-align:center;color:var(--brand);font-weight:800;font-size:17px;letter-spacing:.3px}
.headline{position:absolute;left:0;right:0;top:82px;text-align:center;font-weight:800;font-size:20.5px;line-height:22px}
.rule{position:absolute;top:137px;left:50%;width:117px;height:2px;margin-left:-58px;background:var(--brand)}
.intro{position:absolute;top:158px;left:30px;right:30px;text-align:center;color:var(--grey);font-weight:700;font-size:13.6px;line-height:17px}
.perks{position:absolute;top:251px;left:0;right:0;list-style:none;text-align:center}
.perks li{height:30.5px;font-weight:700;font-size:17px;display:flex;justify-content:center;align-items:center;gap:5px}
.perks svg{width:16px;height:16px}
.photo-socket{position:absolute;left:0;top:399px;width:396px;height:456px;background:linear-gradient(160deg,#f4f5f6,#e6e8ea)}
.calc-box{position:absolute;left:0;top:159px;width:396px;height:471px;background:var(--brand)}
.calc-label{position:absolute;left:0;width:396px;text-align:center;color:var(--white);font-weight:700;font-size:16px}
.calc-field{position:absolute;left:65px;width:265px;height:37px;background:var(--field)}
.calc-field span{position:absolute;right:4px;bottom:1px;font-size:9.5px;color:#4a4f5a;font-weight:600}
.calc-field--result{border:1.5px solid var(--ink)}
.wordmark{position:absolute;left:0;width:396px;text-align:center;color:var(--brand);font-weight:900;display:flex;justify-content:center;align-items:center;gap:10px}
.wordmark i{display:block;border-radius:50%;background:var(--brand)}
.wordmark--contact{top:650px;font-size:42px}
.wordmark--contact i{width:32px;height:32px}
.contact{position:absolute;top:712px;left:0;width:396px;text-align:center;font-weight:700;font-size:16px;line-height:22.5px}
.contact svg{width:13px;height:13px;vertical-align:-1px;margin-right:4px}
.cover-top{position:absolute;left:0;top:0;width:408px;height:212px;background:var(--brand)}
.wordmark--cover{top:64px;width:408px;font-size:52px;color:var(--white)}
.wordmark--cover i{width:46px;height:46px;background:var(--white)}
.cover-rule{position:absolute;top:137px;left:140px;width:118px;height:2px;background:var(--white)}
.cover-sub{position:absolute;top:148px;left:0;width:398px;text-align:center;color:var(--white);font-weight:800;font-size:16px;line-height:20px}
.photo-village{position:absolute;left:0;top:212px;width:408px;height:418px;background:linear-gradient(180deg,#b9c5d3 0%,var(--photo-light) 18%,var(--photo-dark) 55%,#22364f 100%)}
.stats{position:absolute;left:12px;top:591px;width:372px;height:77px;display:flex;box-shadow:0 2px 5px rgba(0,0,0,.2)}
.stat{flex:1;position:relative;background:var(--brand);color:var(--white);text-align:center}
.stat--light{background:var(--white);color:var(--brand)}
.stat-icon{position:absolute;top:-15px;left:50%;margin-left:-15px;width:30px;height:30px;border-radius:3px;background:var(--white);display:flex;align-items:center;justify-content:center}
.stat--light .stat-icon{background:var(--brand)}
.stat-icon svg{width:17px;height:17px}
.stat-label{position:absolute;top:24px;left:0;right:0;font-size:13.5px;font-weight:600}
.stat-value{position:absolute;top:44px;left:0;right:0;font-size:20px;font-weight:900}
.stat--light .stat-value b{color:var(--ink);font-weight:900}
.tagline{position:absolute;top:705px;left:0;width:398px;text-align:center;color:var(--brand);font-weight:900;font-size:38px;line-height:43px;letter-spacing:-1.4px}
.guides{position:absolute;left:0;top:0;pointer-events:none}
</style>
</head>
<body>
<div class="sheet">

  <section class="panel panel--about">
    <p class="eyebrow">ÜBER UNS</p>
    <h2 class="headline">Bürgerenergiegemeinschaft<br>Lindenau an der Rax</h2>
    <div class="rule"></div>
    <p class="intro">Als Bürgerenergiegemeinschaft sind wir für unsere Bürgerinnen und Bürger die erste Anlaufstelle wenn es um sauberen regionalen erneuerbaren Strom geht.</p>
    <ul class="perks">
      <li><svg viewBox="0 0 16 16"><path d="M2 8.5l4 4L14 3" fill="none" stroke="#0ea5dc" stroke-width="2.6"/></svg>Grüne Energie</li>
      <li><svg viewBox="0 0 16 16"><path d="M2 8.5l4 4L14 3" fill="none" stroke="#0ea5dc" stroke-width="2.6"/></svg>Faire Preise</li>
      <li><svg viewBox="0 0 16 16"><path d="M2 8.5l4 4L14 3" fill="none" stroke="#0ea5dc" stroke-width="2.6"/></svg>Regional produziert</li>
      <li><svg viewBox="0 0 16 16"><path d="M2 8.5l4 4L14 3" fill="none" stroke="#0ea5dc" stroke-width="2.6"/></svg>Für jeden</li>
    </ul>
    <div class="photo-socket" role="img" aria-label="Foto: weiße Steckdose mit Stecker und einem Strauß Löwenzahnblüten"></div>
  </section>

  <section class="panel panel--calc">
    <p class="eyebrow">RECHNER</p>
    <h2 class="headline">Zur einfachen &amp; unverbindlichen<br>Kostenabschätzung</h2>
    <div class="rule"></div>
    <div class="calc-box">
      <p class="calc-label" style="top:13px">Abrechnung</p>
      <div class="calc-field" style="top:39px"></div>
      <p class="calc-label" style="top:89px">Energiekosten Bezug</p>
      <div class="calc-field" style="top:113px"><span>Jahresabrechnungskosten in € brutto</span></div>
      <p class="calc-label" style="top:162px">Energiemenge Bezug</p>
      <div class="calc-field" style="top:186px"><span>kWh pro Jahr</span></div>
      <p class="calc-label" style="top:234px">Einspeisevergütung</p>
      <div class="calc-field" style="top:259px"><span>Cent/kWh netto</span></div>
      <p class="calc-label" style="top:308px">Energiemenge Einspeisung</p>
      <div class="calc-field" style="top:332px"><span>kWh pro Jahr</span></div>
      <p class="calc-label" style="top:380px">Ergebnis</p>
      <div class="calc-field calc-field--result" style="top:405px"></div>
    </div>
    <div class="wordmark wordmark--contact"><i></i>KWLRAX</div>
    <p class="contact">
      <svg viewBox="0 0 14 14"><path d="M7 13S2.5 8 2.5 5.2a4.5 4.5 0 019 0C11.5 8 7 13 7 13z" fill="none" stroke="#0ea5dc" stroke-width="1.4"/><circle cx="7" cy="5.3" r="1.5" fill="none" stroke="#0ea5dc" stroke-width="1.3"/></svg>Mühlfeldweg 12<br>
      3290 Lindenau<br>
      <svg viewBox="0 0 14 14"><rect x="1.5" y="3" width="11" height="8.5" rx="1" fill="none" stroke="#0ea5dc" stroke-width="1.4"/><path d="M1.5 3.5L7 8l5.5-4.5" fill="none" stroke="#0ea5dc" stroke-width="1.4"/></svg>info@kwl-rax.example<br>
      <svg viewBox="0 0 14 14"><path d="M1 3h4.5A1.5 1.5 0 017 4.5V12a1.5 1.5 0 00-1.5-1.5H1zM13 3H8.5A1.5 1.5 0 007 4.5V12a1.5 1.5 0 011.5-1.5H13z" fill="none" stroke="#0ea5dc" stroke-width="1.3"/></svg>ZVR-Nr.: 9081726354
    </p>
  </section>

  <section class="panel panel--cover">
    <div class="cover-top"></div>
    <div class="wordmark wordmark--cover"><i></i>KWLRAX</div>
    <div class="cover-rule"></div>
    <p class="cover-sub">Bürgerenergiegemeinschaft<br>Lindenau an der Rax</p>
    <div class="photo-village" role="img" aria-label="Foto in Blautönen: Ortsansicht mit Kirche, Dächern und Hügeln"></div>
    <div class="stats">
      <div class="stat">
        <div class="stat-icon"><svg viewBox="0 0 18 18"><circle cx="6" cy="6" r="2.6" fill="#0ea5dc"/><circle cx="12" cy="6" r="2.6" fill="#0ea5dc"/><path d="M1.5 14a4.5 4 0 019 0zM7.5 14a4.5 4 0 019 0z" fill="#0ea5dc"/></svg></div>
        <p class="stat-label">Zählpunkte</p>
        <p class="stat-value">20+</p>
      </div>
      <div class="stat stat--light">
        <div class="stat-icon"><svg viewBox="0 0 18 18"><circle cx="9" cy="9" r="5" fill="none" stroke="#fff" stroke-width="1.6" stroke-dasharray="2.2 1.3"/><circle cx="9" cy="9" r="2.2" fill="none" stroke="#fff" stroke-width="1.5"/></svg></div>
        <p class="stat-label">PV-Leistung</p>
        <p class="stat-value">&gt; <b>100</b> kWp</p>
      </div>
      <div class="stat">
        <div class="stat-icon"><svg viewBox="0 0 18 18"><path d="M5 2v4M9 2v4M3 6h8v3a4 4 0 01-8 0zM7 13v3" fill="none" stroke="#0ea5dc" stroke-width="1.8"/><circle cx="13" cy="12" r="3.5" fill="#0ea5dc"/><path d="M13.5 10l-1.5 2h2l-1.5 2" fill="none" stroke="#fff" stroke-width="1"/></svg></div>
        <p class="stat-label">Verteilte Energie</p>
        <p class="stat-value">Testphase</p>
      </div>
    </div>
    <p class="tagline">Regionaler Strom<br>für jeden!</p>
  </section>

  <svg class="guides" width="1200" height="855" viewBox="0 0 1200 855">
    <rect x="1" y="1" width="1198" height="853" fill="none" stroke="var(--trim)" stroke-width="1.6"/>
    <rect x="11" y="11" width="1178" height="833" fill="none" stroke="var(--bleed)" stroke-width="2"/>
    <rect x="24" y="24" width="1152" height="807" fill="none" stroke="var(--safe)" stroke-width="2.4" stroke-dasharray="7 5"/>
    <line x1="396" y1="0" x2="396" y2="855" stroke="var(--fold)" stroke-width="2" stroke-dasharray="6 3"/>
    <line x1="792" y1="0" x2="792" y2="855" stroke="var(--fold)" stroke-width="2" stroke-dasharray="6 3"/>
  </svg>
</div>
</body>
</html>
```